Employee I.D. Card - Badge

We need an employee I.D. card designed. Our employees are going to be wearing these. I would like to have it look nice. Something professional yet cool (not uptight if that makes sense).
Project Scope:
Vertical orientation
Company name ------------- (Bright and Tidy)
Website ------------- (brightandtidymn.example)
Employee Picture
background check image
front and back designed - same design on either side
You can create the card without having the employee images on them.
Here are the dimensions -
2.125 x 3.370 inches
Double sided - same design can be used front and back
Background badge - I would like to add an image that shows that the employee has taken a background check. I've added the press-kit for the company we use. If you have a better idea than incorporating their logo, we can certainly do something different.
Example image-
https://www.lookupzone.example/find?q=background+check+badge&kind=images&ref=XyZ4qWm82LpRt:
The print company will set up the names.
Logo is attached
Also attached are our business cards. You can use this for an idea of brand/company style.
Our website - brightandtidymn.example

```html
<!DOCTYPE html>
<html lang="en">
<head>
<meta charset="utf-8">
<title>Bright and Tidy – Employee ID Badge</title>
<link rel="stylesheet" href="https://fonts.googleapis.com/css2?family=Nunito:wght@500;800&family=Oswald:wght@500&display=swap">
<style>
  :root {
    --sky-top: #52c8f8;
    --sky-bottom: #2aa4ec;
    --lime: #c6f200;
    --navy: #0c176c;
    --navy-faint: #26307c;
    --white: #ffffff;
    --ink: #2b2b38;
    --cyan: #33c9f2;
    --brand-blue: #1f9fe3;
    --badge-green: #7ccf1f;
    --photo-light: #dcebf7;
    --photo-mid: #a9c8e4;
  }
  html, body {
    margin: 0;
    padding: 0;
    width: 770px;
    height: 1200px;
    overflow: hidden;
    background: var(--white);
  }
  .badge-card {
    position: relative;
    width: 770px;
    height: 1200px;
    overflow: hidden;
    font-family: "Nunito", sans-serif;
  }
  .card-shapes {
    position: absolute;
    inset: 0;
  }
  .brand-name {
    position: absolute;
    top: 22px;
    right: 40px;
    width: 280px;
    margin: 0;
    text-align: center;
    font-family: "Nunito", sans-serif;
    font-weight: 500;
    font-size: 50px;
    line-height: 0.95;
    color: var(--brand-blue);
  }
  .employee-photo {
    position: absolute;
    left: 52px;
    top: 322px;
    width: 420px;
    height: 456px;
    border-radius: 200px 200px 24px 24px;
    background: linear-gradient(180deg, var(--photo-light) 0%, var(--photo-mid) 100%);
  }
  .check-seal {
    position: absolute;
    left: 340px;
    top: 433px;
    width: 126px;
    height: 126px;
  }
  .employee-name {
    position: absolute;
    left: 478px;
    top: 510px;
    width: 250px;
    margin: 0;
    text-align: center;
    font-family: "Oswald", sans-serif;
    font-weight: 500;
    font-size: 60px;
    line-height: 1.05;
    color: var(--white);
    text-transform: uppercase;
  }
  .employee-role {
    position: absolute;
    left: 478px;
    top: 698px;
    width: 260px;
    margin: 0;
    text-align: center;
    font-family: "Oswald", sans-serif;
    font-weight: 500;
    font-size: 48px;
    line-height: 1;
    color: var(--ink);
    text-transform: uppercase;
  }
  .brand-echo {
    position: absolute;
    left: 385px;
    top: 835px;
    margin: 0;
    font-family: "Nunito", sans-serif;
    font-weight: 500;
    font-size: 130px;
    line-height: 0.9;
    color: var(--navy-faint);
    white-space: nowrap;
  }
  .web-bar {
    position: absolute;
    left: 0;
    top: 1034px;
    width: 770px;
    height: 53px;
    background: var(--white);
  }
  .web-icon {
    position: absolute;
    left: 74px;
    top: 1008px;
    width: 106px;
    height: 106px;
    border-radius: 50%;
    background: var(--white);
    display: flex;
    align-items: center;
    justify-content: center;
  }
  .web-address {
    position: absolute;
    left: 196px;
    top: 1040px;
    margin: 0;
    font-family: "Nunito", sans-serif;
    font-weight: 800;
    font-size: 30px;
    line-height: 40px;
    color: var(--cyan);
  }
</style>
</head>
<body>
<main class="badge-card">
  <svg class="card-shapes" width="770" height="1200" viewBox="0 0 770 1200" aria-hidden="true">
    <defs>
      <linearGradient id="sky" x1="0" y1="0" x2="0" y2="1">
        <stop offset="0" stop-color="var(--sky-top)"/>
        <stop offset="1" stop-color="var(--sky-bottom)"/>
      </linearGradient>
    </defs>
    <rect class="sky-field" width="770" height="700" fill="url(#sky)"/>
    <path class="brand-corner" d="M435 0 H770 V180 C700 150 640 160 560 140 C480 118 470 60 435 0 Z" fill="var(--white)"/>
    <circle class="photo-backdrop" cx="236" cy="726" r="242" fill="var(--white)"/>
    <polygon class="lime-band" points="0,674 770,674 770,813 0,732" fill="var(--lime)"/>
    <polygon class="navy-field" points="0,732 770,813 770,1200 0,1200" fill="var(--navy)"/>
    <g class="bubbles" fill="var(--white)">
      <circle cx="106" cy="470" r="8"/>
      <circle cx="121" cy="466" r="4"/>
      <circle cx="468" cy="576" r="7"/>
      <circle cx="453" cy="585" r="4"/>
    </g>
  </svg>

  <h1 class="brand-name">Bright<br>and Tidy</h1>

  <div class="employee-photo" role="img" aria-label="Employee portrait photo, smiling person in a light blue shirt with arms crossed"></div>

  <svg class="check-seal" viewBox="0 0 126 126" role="img" aria-label="Background check seal">
    <circle cx="63" cy="63" r="60" fill="var(--badge-green)"/>
    <circle cx="63" cy="63" r="42" fill="var(--white)"/>
    <circle cx="63" cy="63" r="20" fill="var(--badge-green)"/>
  </svg>

  <h2 class="employee-name">Employee<br>Name</h2>
  <p class="employee-role">Ocupation</p>

  <p class="brand-echo" aria-hidden="true">bright<br>tidy</p>

  <div class="web-bar"></div>
  <div class="web-icon">
    <svg width="64" height="64" viewBox="0 0 64 64" aria-hidden="true">
      <g fill="none" stroke="var(--brand-blue)" stroke-width="3.5">
        <circle cx="32" cy="32" r="28"/>
        <ellipse cx="32" cy="32" rx="12" ry="28"/>
        <line x1="32" y1="4" x2="32" y2="60"/>
        <line x1="4" y1="32" x2="60" y2="32"/>
        <path d="M9 18 H55 M9 46 H55"/>
      </g>
    </svg>
  </div>
  <p class="web-address">brightandtidymn.example</p>
</main>
</body>
</html>
```